Taskvora Software Business Card Design

We are a new organization called Taskvora. We are a software as a service provider. We deliver a project and program management solution via the internet, so everyone has the ability to work together and collaborate. Its an enterprise platform and we will focus on 50 plus employee company.

We have a website in place
www.taskvora-example.com

Use this as a start of producing the business card. The logo is there as well, but if you have a great and better solution...

Color scheme's could be inline with the website, but don't pin point on it. We can always change the website, logo, color scheme etc.

Target Market(s)

B2B, Projectmembers, projectmanagers, ICT, CTO, Marketing Managers

Industry/Entity Type

Software

Requirements
Must have
• Maarten Velsepol

Tel: +31 555 17 40 92
Mob: +31 6 902 36 517
maarten@taskvora-example.com
Keltenlaan 384b
9071 XK Oostervelde

Www.taskvora-example.com
social media links

```html
<!DOCTYPE html>
<html lang="en">
<head>
<meta charset="utf-8">
<title>Taskvora Business Card</title>
<link rel="stylesheet" href="https://fonts.googleapis.com/css2?family=Open+Sans:wght@300;400;600&display=swap">
<style>
  :root {
    --page-bg: #e8e8e4;
    --card-white: #ffffff;
    --lime: #a9bb2a;
    --lime-light: #b7c52f;
    --lime-text: #9cb626;
    --orange: #f07d1f;
    --white: #ffffff;
    --shadow: rgba(0, 0, 0, 0.18);
  }
  * { margin: 0; padding: 0; box-sizing: border-box; }
  html, body {
    width: 1200px;
    height: 1200px;
    overflow: hidden;
    background: var(--page-bg);
    font-family: "Open Sans", Arial, sans-serif;
  }
  .sheet {
    width: 1200px;
    height: 1200px;
    display: flex;
    flex-direction: column;
    align-items: center;
    justify-content: center;
    gap: 60px;
  }
  .card {
    position: relative;
    width: 900px;
    height: 514px;
    overflow: hidden;
    box-shadow: 0 10px 30px var(--shadow);
  }

  /* Front */
  .card-front { background: var(--card-white); }
  .front-brand {
    position: absolute;
    left: 0; right: 0; top: 180px;
    text-align: center;
  }
  .brand-name {
    font-weight: 300;
    font-size: 86px;
    line-height: 1;
    letter-spacing: 1px;
    color: var(--lime-text);
  }
  .social-links {
    margin-top: 22px;
    display: flex;
    justify-content: center;
    gap: 54px;
    list-style: none;
  }
  .social-links li {
    display: flex;
    align-items: center;
    gap: 8px;
    font-size: 19px;
    font-weight: 600;
    color: var(--orange);
  }
  .social-dot {
    width: 18px; height: 18px;
    border-radius: 50%;
    background: var(--lime-text);
  }

  /* Back */
  .card-back {
    background: linear-gradient(120deg, var(--lime) 0%, var(--lime-light) 100%);
  }
  .back-shape {
    position: absolute;
    inset: 0;
  }
  .back-brand {
    position: absolute;
    left: 120px;
    top: 34px;
  }
  .back-brand .brand-name { font-size: 64px; }
  .back-url {
    margin-top: 6px;
    font-size: 22px;
    color: var(--orange);
  }
  .contact-list {
    position: absolute;
    left: 44px;
    top: 232px;
    list-style: none;
  }
  .contact-list li {
    display: flex;
    align-items: center;
    gap: 12px;
    font-size: 22px;
    line-height: 30px;
    color: var(--white);
  }
  .contact-icon { width: 20px; height: 20px; flex: none; }
  .contact-list .no-icon { padding-left: 32px; }
  .holder-name {
    position: absolute;
    right: 50px;
    bottom: 90px;
    display: flex;
    align-items: flex-end;
    gap: 14px;
    font-weight: 300;
    font-size: 50px;
    line-height: 1;
    color: var(--white);
  }
  .name-bar {
    width: 7px;
    height: 30px;
    background: var(--orange);
    margin-bottom: 2px;
  }
</style>
</head>
<body>
<main class="sheet">

  <section class="card card-front" aria-label="Card front">
    <div class="front-brand">
      <div class="brand-name">Taskvora</div>
      <ul class="social-links">
        <li><span class="social-dot"></span>/Taskvora</li>
        <li><span class="social-dot"></span>/TaskvoraCOM</li>
      </ul>
    </div>
  </section>

  <section class="card card-back" aria-label="Card back">
    <svg class="back-shape" width="900" height="514" viewBox="0 0 900 514" aria-hidden="true">
      <polygon points="90,0 600,0 340,200 90,200" fill="#ffffff"/>
    </svg>

    <div class="back-brand">
      <div class="brand-name">Taskvora</div>
      <div class="back-url">www.taskvora-example.com</div>
    </div>

    <ul class="contact-list">
      <li>
        <svg class="contact-icon" viewBox="0 0 20 20" aria-hidden="true">
          <circle cx="10" cy="10" r="10" fill="#f07d1f"/>
          <path d="M6.5 5.5 l2 0 l1 2.6 l-1.3 1 a6 6 0 0 0 2.7 2.7 l1 -1.3 l2.6 1 l0 2 a1.2 1.2 0 0 1 -1.2 1.2 a8 8 0 0 1 -8 -8 a1.2 1.2 0 0 1 1.2 -1.2z" fill="#ffffff"/>
        </svg>
        +31 555 17 40 92
      </li>
      <li>
        <svg class="contact-icon" viewBox="0 0 20 20" aria-hidden="true">
          <circle cx="10" cy="10" r="10" fill="#f07d1f"/>
          <rect x="7" y="4" width="6" height="12" rx="1.2" fill="#ffffff"/>
          <rect x="8" y="5.5" width="4" height="7.5" fill="#f07d1f"/>
        </svg>
        +31 6 902 36 517
      </li>
      <li>
        <svg class="contact-icon" viewBox="0 0 20 20" aria-hidden="true">
          <circle cx="10" cy="10" r="10" fill="#f07d1f"/>
          <rect x="5" y="6.5" width="10" height="7" fill="#ffffff"/>
          <path d="M5 6.5 l5 4 l5 -4" fill="none" stroke="#f07d1f" stroke-width="1.2"/>
        </svg>
        maarten@taskvora-example.com
      </li>
      <li>
        <svg class="contact-icon" viewBox="0 0 20 20" aria-hidden="true">
          <circle cx="10" cy="10" r="10" fill="#f07d1f"/>
          <path d="M10 4 a4 4 0 0 1 4 4 c0 3 -4 8 -4 8 c0 0 -4 -5 -4 -8 a4 4 0 0 1 4 -4z" fill="#ffffff"/>
          <circle cx="10" cy="8" r="1.5" fill="#f07d1f"/>
        </svg>
        Keltenlaan 384b,
      </li>
      <li class="no-icon">9071 XK Oostervelde</li>
    </ul>

    <div class="holder-name">Maarten Velsepol<span class="name-bar"></span></div>
  </section>

</main>
</body>
</html>
```